Business Card Design

We have recently seen two business cards that caught our attention and think the designs would work for us. We are an accounting firm that serves small businesses in a variety of industries. Attached are the two business card that inspired us along with very rough layouts. We would like to see a professional layout using our company information.

Industry/Entity Type

Accounting

Contact Information for Business Card

Company Name - Dalworth Pryce
Address - 4180 Brambleton Lane, Suite 310, Houston, TX 77051
713-508-9627 - Main
281-369-0714 - Fax

Team Member Names, emails and phone numbers (see attachment)

```html
<!DOCTYPE html>
<html lang="en">
<head>
<meta charset="utf-8">
<title>Dalworth Pryce — Business Card</title>
<link href="https://fonts.googleapis.com/css2?family=Cinzel:wght@500;600&family=Exo+2:wght@400;500&display=swap" rel="stylesheet">
<style>
  :root {
    --canvas: #e4e4e4;
    --paper: #ffffff;
    --charcoal: #3a3a3c;
    --swoosh: #b9b9bb;
    --ink: #2e2e30;
    --ink-soft: #555558;
    --on-dark: #f2f2f2;
  }
  * { margin: 0; padding: 0; box-sizing: border-box; }
  html, body { width: 1200px; height: 900px; overflow: hidden; }
  body {
    background: var(--canvas);
    display: flex; flex-direction: column;
    align-items: center; justify-content: center; gap: 60px;
  }
  .card {
    position: relative; width: 630px; height: 360px;
    background: var(--paper); border-radius: 28px; overflow: hidden;
    box-shadow: 0 6px 18px rgba(0,0,0,.15);
  }
  .card-front { display: flex; align-items: center; justify-content: center; }
  .company-name {
    font-family: "Cinzel", serif; font-weight: 600;
    color: var(--ink); letter-spacing: 2px; white-space: nowrap;
  }
  .card-front .company-name { font-size: 46px; }
  .card-back .backdrop { position: absolute; inset: 0; }
  .card-back .company-name {
    position: absolute; left: 38px; top: 190px; font-size: 26px;
  }
  .person {
    position: absolute; left: 120px; top: 36px; width: 200px; text-align: right;
    font-family: "Exo 2", sans-serif; text-transform: uppercase; color: var(--ink);
    white-space: nowrap;
  }
  .person-name { font-size: 17px; font-weight: 500; letter-spacing: 1px; }
  .person-title { font-size: 11px; letter-spacing: 1.5px; color: var(--ink-soft); margin-top: 2px; }
  .contact-list {
    position: absolute; right: 24px; top: 34px; list-style: none;
    font-family: "Exo 2", sans-serif; font-size: 12px; color: var(--on-dark);
  }
  .contact-list li {
    display: flex; justify-content: flex-end; align-items: center; gap: 9px;
    height: 23px; letter-spacing: .4px; white-space: nowrap;
  }
  .contact-list svg { width: 13px; height: 13px; flex: none; }
  .address {
    position: absolute; right: 24px; bottom: 28px; text-align: right; width: 250px;
    font-family: "Exo 2", sans-serif; font-size: 12px; line-height: 1.45;
    color: var(--on-dark); letter-spacing: .4px;
  }
</style>
</head>
<body>
  <section class="card card-front">
    <h1 class="company-name">Dalworth Pryce</h1>
  </section>

  <section class="card card-back">
    <svg class="backdrop" viewBox="0 0 630 360" aria-hidden="true">
      <path d="M330 0 C400 90 370 250 150 360 L630 360 L630 0 Z" fill="var(--swoosh)"/>
      <path d="M362 0 C432 90 404 255 192 360 L630 360 L630 0 Z" fill="var(--paper)"/>
      <path d="M374 0 C444 90 418 258 212 360 L630 360 L630 0 Z" fill="var(--charcoal)"/>
    </svg>

    <div class="person">
      <div class="person-name">Owen Hartley</div>
      <div class="person-title">Financial Advisor</div>
    </div>

    <div class="company-name">Dalworth Pryce</div>

    <ul class="contact-list">
      <li>713-508-9627
        <svg viewBox="0 0 16 16"><path d="M3 1h3l1.5 4-2 1.3a9 9 0 0 0 4.2 4.2L11 8.5l4 1.5v3a2 2 0 0 1-2 2A13 13 0 0 1 1 3a2 2 0 0 1 2-2z" fill="var(--on-dark)"/></svg>
      </li>
      <li>281-369-0714
        <svg viewBox="0 0 16 16"><rect x="4" y="1" width="8" height="5" fill="none" stroke="var(--on-dark)" stroke-width="1.4"/><rect x="1" y="6" width="14" height="8" rx="1.5" fill="var(--on-dark)"/></svg>
      </li>
      <li>713-508-9630
        <svg viewBox="0 0 16 16"><rect x="4" y="1" width="8" height="14" rx="1.5" fill="var(--on-dark)"/><rect x="5.5" y="3" width="5" height="8" fill="var(--charcoal)"/></svg>
      </li>
      <li>owen@dalworthpryce.com
        <svg viewBox="0 0 16 16"><rect x="1" y="3" width="14" height="10" rx="1" fill="var(--on-dark)"/><path d="M1.5 3.5 8 9l6.5-5.5" fill="none" stroke="var(--charcoal)" stroke-width="1.2"/></svg>
      </li>
      <li>www.dalworthpryce.com
        <svg viewBox="0 0 16 16"><circle cx="8" cy="8" r="6.5" fill="none" stroke="var(--on-dark)" stroke-width="1.4"/><path d="M1.5 8h13M8 1.5c-3 3.5-3 9.5 0 13M8 1.5c3 3.5 3 9.5 0 13" fill="none" stroke="var(--on-dark)" stroke-width="1.1"/></svg>
      </li>
    </ul>

    <p class="address">4180 Brambleton Lane, Suite 310<br>Houston, TX 77051</p>
  </section>
</body>
</html>
```